Brightmorrow - a website to encourage people to spend time in nature

I have a squarespace site with some content on it but the squarespace template doesn't completely suit my needs, I keep fiddling with the template but actually I need some professional help to get it looking the way I want and with the right 'mood'.
The website is for "Brightmorrow" - it will be a blog where I write about the importance of nature for good health. I also want to use the website to market services such as outdoor coaching, retreats and walking workshops.
This has been in my head for a LONG time and I currently only use instagram for micro-blogs but it's time for me to get this moving. I've previously engaged other designers on branding for it but they just didn't get it quite the way that I wanted it and I wasn't completely happy with the results. It's been a process for me as to what I want but in the meantime I just didn't come back to the design aspect of it now. I'm looking for a designer who understands the purpose of the website, the ethos and can help me realise this into a design that's clean, clear and simple.

Please note that I have a domain (brightmorrow.example) and a lot of content drafted on squarespace already. I have published it with password protection - password is brightmorrow2020 - it still has some of the original template on it, but does have some content. Don't take it as anything to follow in particular, i am looking for fresh eyes and fresh ideas.
Updates

Need extra days to review

Target Market(s)

There are three main groups that I want to target - people who are suffering from stress and anxiety, people who treat them and parents who want to get their kids outside (thereby preventing stress and anxiety)

Contact Information for Business Card

Clara Dunmore
Brightmorrow
Telephone +44 7946 203857
brightmorrow@mailbox.example

Logo Text

Brightmorrow - if that. I have an idea that the logo should have a leaf on it somewhere, or maybe just be a leaf.

Coding

Coded - Design and coding required

Number of Pages Required

5+ page

Font styles to use
Serif
Sans Serif

Colors
add136
33b8a4
34a6d7
3377b5

Requirements
Must have
• Space for lots of images. The ability for me to edit the pages if I need to. Be user friendly. Look beautiful.
• For an idea of the images I use and the content I'm interested in writing about have a look at @brightmorrow on instagram.
• That pop up about cookies so I am complying with data laws.
Should not have
• Must not be too 'busy' I'd like to avoid too much movement.

```html
<!DOCTYPE html>
<html lang="en">
<head>
<meta charset="utf-8">
<title>Brightmorrow</title>
<link href="https://fonts.googleapis.com/css2?family=Itim&family=Lora:wght@400;500&family=Raleway:wght@400;500;600&display=swap" rel="stylesheet">
<style>
:root{
  --mint:#a6ddd2;
  --mint-pale:#e3f0ee;
  --sea:#d5ebe6;
  --paper:#f5f5f5;
  --blue:#3377b5;
  --blue-soft:#5b9ac9;
  --ink:#222;
  --grey:#777;
  --dark:#2f2f2f;
  --white:#fff;
}
*{box-sizing:border-box;margin:0;padding:0}
html,body{width:1200px;height:4389px;overflow:hidden}
body{position:relative;background:var(--paper);font-family:'Raleway',sans-serif;color:var(--ink)}
.abs{position:absolute}
.display{font-family:'Itim',cursive}

/* top bar */
.topbar{left:0;top:0;width:1200px;height:34px;background:var(--mint)}
.topbar .dots{left:60px;top:11px;display:flex;gap:8px}
.dot{width:11px;height:11px;border-radius:50%;background:#2c4a46}
.topbar .search{right:110px;top:10px;font-size:9px;color:#333;display:flex;gap:10px;align-items:center}
.topbar .menu{right:52px;top:11px}

/* header */
.header{left:0;top:34px;width:1200px;height:153px;background:var(--paper)}
.brand{left:0;width:1200px;top:22px;text-align:center;font-size:58px;font-weight:400;color:var(--ink);letter-spacing:1px}
.tagline{left:0;width:1200px;top:102px;text-align:center;font-size:13px;color:var(--grey);letter-spacing:.5px}

/* hero */
.hero{left:0;top:187px;width:1200px;height:495px;background:var(--mint-pale)}
.hero-photo{left:61px;top:36px;width:696px;height:426px;background:linear-gradient(135deg,#c78aa0 0%,#9a8b6a 40%,#c4a27a 65%,#6f7f55 100%)}
.hero-photo .welcome{left:26px;top:48px;color:var(--white);font-size:31px;line-height:1;opacity:.9}
.hero-photo .welcome span{display:block;font-size:54px;margin-top:6px}
.video-tile{left:776px;top:36px;width:322px;height:203px;background:linear-gradient(180deg,#9fbf7a 0%,#c9d6a4 45%,#6f9a48 100%)}
.video-tile .label{left:0;top:0;width:124px;height:72px;background:#9ccc3f;color:var(--white);padding:6px 10px;font-size:30px;line-height:.9}
.video-tile .label span{display:block;font-size:21px}
.video-tile svg{right:16px;bottom:10px}
.more-blogs{left:776px;top:260px;width:320px;height:202px;background:var(--blue);color:var(--white);font-size:31px;letter-spacing:3px;display:flex;align-items:center;justify-content:center}
.social-rail{left:0;top:290px;width:38px;height:171px;background:var(--white);display:flex;flex-direction:column;align-items:center;justify-content:center;gap:19px}
.social-rail .dot{background:#333;width:10px;height:10px}

/* subscribe band */
.subscribe{left:138px;top:740px;width:926px;height:182px;background:var(--mint)}
.sub-title{font-size:38px;letter-spacing:4px;color:var(--ink);line-height:1}
.sub-kicker{font-size:13px;letter-spacing:3px;color:var(--blue)}
.subscribe .sub-title{left:89px;top:60px}
.subscribe .sub-kicker{left:90px;top:100px}
.field{background:var(--white);border-radius:4px;font-size:12px;color:#bbb;padding:0 28px;display:flex;align-items:center}
.subscribe .field{left:322px;top:71px;width:385px;height:41px}
.btn{background:var(--blue);color:var(--white);border-radius:4px;box-shadow:0 3px 6px rgba(0,0,0,.25);display:flex;align-items:center;justify-content:center;font-family:'Itim',cursive;letter-spacing:2px;font-size:14px}
.subscribe .btn{left:721px;top:71px;width:123px;height:41px}

/* author strip */
.rule{left:0;top:1000px;width:506px;height:5px;background:var(--blue)}
.author{left:0;top:1006px;width:852px;height:238px;background:var(--mint-pale)}
.author-photo{left:66px;top:40px;width:178px;height:178px;border-radius:50%;background:radial-gradient(circle at 40% 40%,#e8ddc8 0%,#a9a296 55%,#3b3b3b 100%)}
.author .hello{left:274px;top:114px;font-family:'Itim',cursive;font-size:17px;letter-spacing:1px}
.author .bio{left:274px;top:140px;font-size:13px;color:#555;letter-spacing:.5px}
.author .ig{left:274px;top:166px;width:13px;height:13px;border:1.6px solid #333;border-radius:50%}
.author-block{left:852px;top:980px;width:348px;height:287px;background:var(--blue)}
.author-inset{left:852px;top:1006px;width:86px;height:238px;background:var(--blue-soft);border-radius:0 6px 6px 0}

/* about */
.section-title{left:0;width:1200px;text-align:center;font-family:'Itim',cursive;font-weight:400;color:var(--ink)}
.about-title{top:1336px;font-size:55px}
.origin{left:95px;top:1466px;width:505px;height:503px;border-radius:4px;background:linear-gradient(180deg,#6b9ad4 0%,#5887c2 50%,#5d7e9e 100%);color:var(--white)}
.origin h3{position:absolute;left:54px;top:110px;font-family:'Itim',cursive;font-weight:400;font-size:30px}
.origin .kicker{left:54px;top:164px;font-size:16px;letter-spacing:2px}
.origin p{position:absolute;left:54px;top:192px;width:400px;font-size:13.5px;line-height:23px;letter-spacing:1.3px}
.btn-ghost{background:var(--white);color:var(--blue);border-radius:4px;font-family:'Itim',cursive;letter-spacing:2px;font-size:14px;display:flex;align-items:center;justify-content:center}
.origin .btn-ghost{left:54px;top:350px;width:143px;height:41px}
.blossom{left:619px;top:1466px;width:179px;height:244px;background:linear-gradient(135deg,#f1a9c4 0%,#cc4f7f 45%,#f4c7d8 75%,#7a3b4f 100%)}
.shore{left:619px;top:1725px;width:179px;height:244px;background:linear-gradient(180deg,#3f6fc4 0%,#9cb9de 45%,#7d7468 60%,#5a524a 100%)}
.feature h4{font-family:'Itim',cursive;font-weight:400;font-size:30px;color:var(--ink)}
.feature p{margin-top:14px;font-size:13.5px;line-height:23px;letter-spacing:1.3px;color:#888}
.feature .btn{position:relative;margin-top:16px;width:135px;height:40px}
.what{left:827px;top:1508px;width:290px}
.partners{left:828px;top:1741px;width:290px}

/* blogs */
.blogs{left:0;top:2083px;width:1200px;height:1739px;background:var(--sea)}
.blogs-title{top:88px;font-size:55px}
.blogs-sub{left:0;top:180px;width:1200px;text-align:center;font-family:'Itim',cursive;font-size:31px;color:var(--blue)}
.blogs-date{left:0;top:242px;width:1200px;text-align:center;font-size:19px;color:#555;font-weight:500}
.blogs-rule{left:585px;top:287px;width:30px;height:2px;background:#666}
.post{width:324px;text-align:center}
.post .photo{width:324px;height:324px}
.post h5{margin-top:55px;font-family:'Lora',serif;font-weight:400;font-size:25px;line-height:34px;color:#333;letter-spacing:.5px}
.post p{margin:30px auto 0;width:290px;font-size:14.5px;line-height:26px;color:#666}
.post .more{margin-top:20px;font-family:'Lora',serif;font-size:13px;color:var(--blue);display:flex;gap:10px;justify-content:center;align-items:center}
.c1{left:70px}.c2{left:435px}.c3{left:799px}
.r1{top:363px}.r2{top:1029px}

/* contact */
.contact{left:0;top:3822px;width:1200px;height:282px;background:#f3f3f3}
.contact-title{top:48px;font-size:57px}
.contact .note{left:0;top:134px;width:1200px;text-align:center;font-size:13px;letter-spacing:2px;color:#888}
.contact .btn{left:387px;top:185px;width:426px;height:40px;font-size:13px}

/* footer */
.footer{left:0;top:4104px;width:1200px;height:220px;background:var(--blue)}
.footer .sub-title{left:63px;top:76px;color:#1d2a3a}
.footer .sub-kicker{left:63px;top:118px;color:#1d2a3a}
.footer .field{left:297px;top:89px;width:383px;height:41px}
.footer .btn{left:700px;top:89px;width:116px;height:41px}
.footer .icons{left:1026px;top:170px;display:flex;gap:18px;align-items:center}
.footer .icons .dot{background:var(--white);width:15px;height:15px}
.bottombar{left:0;top:4324px;width:1200px;height:65px;background:var(--dark);color:var(--white);font-size:14px;display:flex;align-items:center;justify-content:center;gap:8px;letter-spacing:.5px}
.bottombar .copy{width:18px;height:18px;border:1.5px solid var(--white);border-radius:50%;font-size:11px;display:flex;align-items:center;justify-content:center}
</style>
</head>
<body>

<div class="abs topbar">
  <div class="abs dots"><span class="dot"></span><span class="dot"></span><span class="dot"></span><span class="dot"></span></div>
  <div class="abs search">search
    <svg width="12" height="12" viewBox="0 0 12 12"><circle cx="5" cy="5" r="3.6" fill="none" stroke="#222" stroke-width="1.5"/><line x1="7.7" y1="7.7" x2="11" y2="11" stroke="#222" stroke-width="1.5"/></svg>
  </div>
  <svg class="abs menu" width="16" height="12" viewBox="0 0 16 12"><rect y="0" width="16" height="2" fill="#222"/><rect y="5" width="16" height="2" fill="#222"/><rect y="10" width="16" height="2" fill="#222"/></svg>
</div>

<header class="abs header">
  <h1 class="abs brand display">Brightmorrow</h1>
  <p class="abs tagline">The practice of spending time in nature to feel better.</p>
</header>

<section class="abs hero">
  <div class="abs hero-photo" role="img" aria-label="Woman laughing on a bicycle among pink flowering shrubs">
    <div class="abs welcome display">Welcome To<span>Brightmorrow</span></div>
  </div>
  <div class="abs video-tile" role="img" aria-label="Two children lying in a grassy meadow">
    <div class="abs label display">Video<span>Blogs</span></div>
    <svg class="abs" width="32" height="32" viewBox="0 0 32 32"><circle cx="16" cy="16" r="14" fill="none" stroke="#fff" stroke-width="2"/><path d="M13 10 L22 16 L13 22 Z" fill="#fff"/></svg>
  </div>
  <div class="abs more-blogs display">More Blogs</div>
  <div class="abs social-rail"><span class="dot"></span><span class="dot"></span><span class="dot"></span>
    <svg width="11" height="8" viewBox="0 0 11 8"><rect x=".5" y=".5" width="10" height="7" fill="none" stroke="#333"/><path d="M.5 .5 L5.5 4.5 L10.5 .5" fill="none" stroke="#333"/></svg>
  </div>
</section>

<section class="abs subscribe">
  <div class="abs sub-title display">Subscribe</div>
  <div class="abs sub-kicker display">Stay Connected</div>
  <div class="abs field">Email</div>
  <div class="abs btn">Sign up</div>
</section>

<div class="abs rule"></div>
<section class="abs author">
  <div class="abs author-photo" role="img" aria-label="Portrait of the author in sunglasses"></div>
  <div class="abs hello">Welcome to Brightmorrow.</div>
  <div class="abs bio">I document the relationship between nature and better health.</div>
  <div class="abs ig"></div>
</section>
<div class="abs author-block"></div>
<div class="abs author-inset"></div>

<h2 class="abs section-title about-title">About Us</h2>
<article class="abs origin" role="img" aria-label="Woman looking out over the sea, tinted blue">
  <h3>Origin Story</h3>
  <div class="abs kicker">In The Beginning...</div>
  <p>Brightmorrow Was Founded In 2017 By Me, Clara Dunmore,&nbsp; A Recovering Lawyer/Corporate Junkie. I Had Spent Most Of The Previous Fifteen Years In Offices In London And For Many Of Those Years I Had Been Sedentry, Stressed And Ill-At-Ease With Myself.</p>
  <div class="abs btn-ghost">Read More</div>
</article>
<div class="abs blossom" role="img" aria-label="Pink cherry blossom against blue sky"></div>
<div class="abs shore" role="img" aria-label="Dog and long shadows on a sandy beach"></div>
<div class="abs feature what">
  <h4>What We Do</h4>
  <p>We Do Some Things That Will Help You Get Back To Nature.</p>
  <div class="btn">Read More</div>
</div>
<div class="abs feature partners">
  <h4>Partners</h4>
  <p>We Believe We Work Better When We Work Together.&nbsp; We Are Proud To Work Together With These Organisations.</p>
  <div class="btn">Read More</div>
</div>

<section class="abs blogs">
  <h2 class="abs section-title blogs-title">Blogs</h2>
  <div class="abs blogs-sub">Good for you. Good for the plannet</div>
  <div class="abs blogs-date">Feb 14</div>
  <div class="abs blogs-rule"></div>

  <article class="abs post c1 r1">
    <div class="photo" role="img" aria-label="Autumn park and city skyline under a rainbow" style="background:linear-gradient(180deg,#8d8a80 0%,#a89a6e 45%,#7a6a26 75%,#4d4a1c 100%)"></div>
    <h5>Why being outside is<br>good for the planet</h5>
    <p>The focus of Brightmorrow is on people. Making people feel better through time spent in nature...</p>
    <div class="more">Read More <svg width="18" height="10" viewBox="0 0 18 10"><path d="M0 5 H16 M12 1 L16 5 L12 9" fill="none" stroke="#3377b5" stroke-width="1.4"/></svg></div>
  </article>
  <article class="abs post c2 r1">
    <div class="photo" role="img" aria-label="Sun shining through bare trees" style="background:radial-gradient(circle at 35% 62%,#f4f1e6 0%,#5a7fc0 25%,#2a4b9a 55%,#101522 100%)"></div>
    <h5>Thank Gerald<br>Pemberton copy</h5>
    <p>I had had a lot of thoughts about creating Brightmorrow for a while. No real direction or goal...</p>
    <div class="more">Read More <svg width="18" height="10" viewBox="0 0 18 10"><path d="M0 5 H16 M12 1 L16 5 L12 9" fill="none" stroke="#3377b5" stroke-width="1.4"/></svg></div>
  </article>
  <article class="abs post c3 r1">
    <div class="photo" role="img" aria-label="Bird nesting in a gap of a weathered white wall" style="background:radial-gradient(circle at 50% 50%,#4a3a2a 0%,#9a9691 25%,#c8c6c2 60%,#b1afab 100%)"></div>
    <h5>Notes From the Nest</h5>
    <p>Growing up in this part of the world, I had the best playground. There are plenty of grainy...</p>
    <div class="more">Read More <svg width="18" height="10" viewBox="0 0 18 10"><path d="M0 5 H16 M12 1 L16 5 L12 9" fill="none" stroke="#3377b5" stroke-width="1.4"/></svg></div>
  </article>

  <article class="abs post c1 r2">
    <div class="photo" role="img" aria-label="Trees reflected in a red pool with red parasols" style="background:linear-gradient(180deg,#5e7a3a 0%,#dfe3e0 35%,#cf2a25 60%,#8a1210 100%)"></div>
    <h5>In The Beginning<br>There Was Pemberton</h5>
    <p>The focus of Brightmorrow is on people. Making people feel better through time spent in nature...</p>
    <div class="more">Read More</div>
  </article>
  <article class="abs post c2 r2">
    <div class="photo" role="img" aria-label="Grey and white clouds across the sky" style="background:linear-gradient(160deg,#8e99a8 0%,#d9dde2 40%,#a2acb8 70%,#c8ccd2 100%)"></div>
    <h5>Skytime Over<br>Screentime</h5>
    <p>I had had a lot of thoughts about creating Brightmorrow for a while. No real direction or goal...</p>
    <div class="more">Read More</div>
  </article>
  <article class="abs post c3 r2">
    <div class="photo" role="img" aria-label="Child in a wildflower meadow with wind turbines behind" style="background:linear-gradient(180deg,#a9c0d8 0%,#c8d3dc 28%,#5f7a3a 50%,#3b5a22 80%,#c9a62a 100%)"></div>
    <h5>On the Verge</h5>
    <p>Growing up in this part of the world, I had the best playground. There are plenty of grainy...</p>
    <div class="more">Read More</div>
  </article>
</section>

<section class="abs contact">
  <h2 class="abs section-title contact-title">Contact us</h2>
  <div class="abs note">Email Me For Press/Media Inquiries And Other Collaborations.</div>
  <div class="abs btn">hello@brightmorrow.example</div>
</section>

<footer class="abs footer">
  <div class="abs sub-title display">Subscribe</div>
  <div class="abs sub-kicker display">Stay Connected</div>
  <div class="abs field">Email</div>
  <div class="abs btn">Sign up</div>
  <div class="abs icons"><span class="dot"></span><span class="dot"></span><span class="dot"></span>
    <svg width="16" height="12" viewBox="0 0 16 12"><rect x=".75" y=".75" width="14.5" height="10.5" fill="none" stroke="#fff" stroke-width="1.5"/><path d="M.75 .75 L8 6.5 L15.25 .75" fill="none" stroke="#fff" stroke-width="1.5"/></svg>
  </div>
</footer>
<div class="abs bottombar"><span class="copy">C</span>Copyright@Brightmorrow2019</div>

</body>
</html>
```